Web Design Project

Psychotherapist in Private Practice
Practice name "The Steady Harbor"
The population is professional adults seeking life coaching and change consultation
I am including a photo for inspiration ONLY - It includes the theme of light and tree branches. There does not HAVE to be a photograph . An illustration , concept or theme of nature /light / generativity / growth / creativity is acceptable
Clean sharp lines Light colors, minimalist , modern.
There is a separate project for a logo design that will become part of the web design
Here are examples of two logos/websites I like
http://www.quietrivergroup.example/
http://www.brightknollpartners.example/

Target Market(s)

Professional adults seeking life coaching

Industry/Entity Type

Life Coaching

Requirements
Should not have
• Although the business name has 'compassion' in it, designs with hearts in it would have to be pretty stylish, subtle, mature and sophisticated to be considered.

```html
<!DOCTYPE html>
<html lang="en">
<head>
<meta charset="utf-8">
<title>The Steady Harbor — Psychotherapy and Consulting</title>
<link rel="stylesheet" href="https://fonts.googleapis.com/css2?family=Open+Sans:ital,wght@0,400;0,600;0,700;1,400&family=Questrial&family=Italianno&display=swap">
<style>
  :root {
    --nav-bg: #2a130c;
    --nav-dash: #b8926a;
    --ink: #2b1d14;
    --body-text: #2d2d2d;
    --muted: #8a8a8a;
    --link-blue: #1d5fb8;
    --sun-light: #fff3a8;
    --sun-mid: #f4b640;
    --dusk: #6d4b44;
    --about: #f1c94a;
    --what: #b1d874;
    --member: #d7d7d7;
    --footer-bg: #dedede;
    --footer-card: #ececec;
    --rule: #cfcfcf;
  }
  html, body { margin: 0; padding: 0; overflow: hidden; background: #ffffff; }
  .canvas {
    position: relative;
    width: 946px;
    height: 1200px;
    overflow: hidden;
    background: #ffffff;
    font-family: "Open Sans", sans-serif;
    color: var(--body-text);
  }
  .abs { position: absolute; }

  /* Navigation */
  .main-nav {
    position: absolute; left: 0; top: 0; width: 946px; height: 47px;
    background: var(--nav-bg);
  }
  .main-nav::before, .main-nav::after {
    content: ""; position: absolute; left: 0; right: 0;
    border-top: 1px dashed var(--nav-dash); opacity: .7;
  }
  .main-nav::before { top: 2px; }
  .main-nav::after { bottom: 2px; }
  .main-nav a {
    position: absolute; top: 12px;
    color: #ffffff; text-decoration: none;
    font-family: "Open Sans", sans-serif; font-size: 17px; line-height: 22px;
  }

  /* Hero */
  .hero-bg { position: absolute; left: 0; top: 47px; width: 946px; height: 500px; }
  .brand-name {
    position: absolute; left: 120px; top: 78px;
    font-family: "Open Sans", sans-serif; font-weight: 600;
    font-size: 40px; line-height: 48px; color: #ffffff;
    letter-spacing: .5px;
  }
  .slide-photo {
    position: absolute; left: 93px; top: 176px; width: 597px; height: 280px;
    background: linear-gradient(180deg, #e9a83a 0%, #f6c64a 32%, #d9622a 52%, #6b3a2a 72%, #2c1a16 100%);
    box-shadow: 0 8px 18px rgba(60, 30, 20, .45);
  }
  .slide-caption {
    position: absolute; left: 24px; bottom: 20px;
    font-family: "Questrial", sans-serif; font-size: 19px; letter-spacing: .6px;
    color: #ffffff; text-transform: uppercase;
  }
  .slider-dots { position: absolute; left: 317px; top: 468px; display: flex; gap: 11px; }
  .slider-dots span { width: 13px; height: 13px; border-radius: 50%; background: #111111; display: block; }
  .hero-tagline {
    position: absolute; left: 714px; top: 189px; width: 232px;
    font-family: "Questrial", sans-serif; font-variant: small-caps;
    font-size: 23px; line-height: 26.5px; letter-spacing: 1px; color: #1c130d;
  }
  .hero-figure {
    position: absolute; left: 729px; top: 402px; width: 90px; height: 100px;
    background: radial-gradient(ellipse at center, rgba(30,16,10,.85) 0%, rgba(30,16,10,.35) 55%, rgba(30,16,10,0) 75%);
  }

  /* Welcome */
  .welcome-title {
    position: absolute; left: 0; width: 836px; top: 492px; text-align: center;
    font-family: "Italianno", cursive; font-size: 36px; line-height: 40px; color: #1a1a1a;
  }
  .welcome-photo {
    position: absolute; left: 92px; top: 546px; width: 143px; height: 104px;
    border: 1px solid #b9b9b9;
    background: linear-gradient(135deg, #dfe3e6 0%, #c9b6a4 45%, #7a5a46 70%, #c9d2da 100%);
  }
  .welcome-copy {
    position: absolute; left: 262px; top: 545px; width: 612px;
    font-size: 10.6px; line-height: 14.2px; color: var(--body-text);
  }
  .welcome-copy p { margin: 0 0 14.2px; }
  .section-rule { position: absolute; left: 92px; top: 672px; width: 774px; border-top: 1px solid #e6e6e6; }
  .read-more-line {
    position: absolute; right: 80px; top: 663px;
    font-size: 13px; color: #222222; text-decoration: none;
  }

  /* Feature circles */
  .feature {
    position: absolute; top: 721px; width: 228px; height: 228px; border-radius: 50%;
  }
  .feature::after {
    content: ""; position: absolute; left: 49px; top: 229px; width: 130px; height: 22px;
    border-radius: 50%;
    background: radial-gradient(ellipse at center, rgba(110,90,50,.55) 0%, rgba(110,90,50,0) 70%);
  }
  .feature-about { left: 93px; background: var(--about); }
  .feature-what { left: 347px; background: var(--what); }
  .feature-member { left: 600px; background: var(--member); }
  .feature h2 {
    margin: 0; position: absolute; left: 0; right: 0; top: 33px; text-align: center;
    font-weight: 400; font-size: 20.5px; line-height: 24px; color: #2a2117;
  }
  .feature h2::after {
    content: ""; display: block; width: 88px; margin: 5px auto 0;
    border-top: 1px solid rgba(255,255,255,.6);
  }
  .feature .feature-text {
    position: absolute; left: 33px; top: 76px; width: 172px;
    font-size: 10.7px; line-height: 14.2px; color: #2a2a2a;
  }
  .feature .feature-text p { margin: 0 0 14.2px; }
  .feature .feature-link {
    position: absolute; left: 0; right: 0; top: 193px; text-align: center;
    font-size: 13px; color: #222222; text-decoration: none;
  }

  /* Footer */
  .site-footer {
    position: absolute; left: 0; top: 989px; width: 946px; height: 211px;
    background: linear-gradient(180deg, #d8d8d8 0%, var(--footer-bg) 30%, #e2e2e2 100%);
    border-top: 3px double #b9b9b9;
  }
  .footer-heading { position: absolute; font-size: 14px; color: #222222; }
  .more-pill {
    position: absolute; left: 274px; top: 28px; width: 42px; height: 17px; border-radius: 9px;
    background: linear-gradient(180deg, #8a8a8a, #4a4a4a);
    color: #ffffff; font-size: 7px; line-height: 17px; text-align: left; padding-left: 8px; box-sizing: border-box;
  }
  .more-pill::after {
    content: ""; position: absolute; right: 8px; top: 6px;
    border-left: 4px solid #ffffff; border-top: 3px solid transparent; border-bottom: 3px solid transparent;
  }
  .news-item {
    position: absolute; left: 111px; width: 204px; height: 42px; background: var(--footer-card);
  }
  .news-item .news-title {
    position: absolute; left: 7px; top: 6px; width: 188px; padding-bottom: 2px;
    border-bottom: 1px solid #c8c8c8;
    font-size: 9.5px; font-weight: 700; color: #333333;
  }
  .news-item .news-date { color: var(--link-blue); margin-right: 4px; }
  .news-item .news-by {
    position: absolute; left: 46px; top: 26px; font-size: 9.5px; font-style: italic; color: var(--muted);
  }
  .footer-divider { position: absolute; top: 28px; height: 166px; border-left: 1px solid var(--rule); }
  .contact-name {
    position: absolute; left: 372px; top: 60px; width: 221px; padding-bottom: 3px;
    border-bottom: 1px solid var(--rule);
    font-size: 11px; color: var(--link-blue); text-transform: uppercase;
  }
  .contact-lines {
    position: absolute; left: 372px; top: 84px; font-size: 9.8px; line-height: 17.3px; color: #333333;
  }
  .contact-lines a { color: var(--link-blue); text-decoration: none; font-size: 11px; }
  .contact-map {
    position: absolute; left: 489px; top: 85px; width: 102px; height: 76px;
    border: 2px solid #ffffff;
    background: linear-gradient(135deg, #e9e2c8 0%, #d7d4c2 50%, #c7d2b8 100%);
  }
  .footer-brand {
    position: absolute; left: 647px; top: -2px; width: 179px; height: 64px; background: #000000;
    display: flex; align-items: center; justify-content: center;
    color: #ffffff; font-size: 15px; font-weight: 400;
  }
  .copyright {
    position: absolute; left: 649px; top: 88px; font-size: 9.3px; line-height: 16px; color: #444444;
  }
</style>
</head>
<body>
<div class="canvas">

  <nav class="main-nav">
    <a href="#" style="left:68px">Home</a>
    <a href="#" style="left:149px">Programs</a>
    <a href="#" style="left:260px">Success Stories</a>
    <a href="#" style="left:411px">Free Resources</a>
    <a href="#" style="left:562px">Blog</a>
    <a href="#" style="left:634px">Contact Us</a>
    <a href="#" style="left:751px">Affiliate Program</a>
  </nav>

  <svg class="hero-bg" width="946" height="500" viewBox="0 0 946 500" role="img" aria-label="Sunset sky with tree branches over the sea">
    <defs>
      <linearGradient id="skyWarm" x1="0" y1="0" x2="1" y2="0.3">
        <stop offset="0" stop-color="#7a5a52"/>
        <stop offset="0.35" stop-color="#c9873e"/>
        <stop offset="0.7" stop-color="#f6d86a"/>
        <stop offset="1" stop-color="#fff6b0"/>
      </linearGradient>
      <linearGradient id="skyFade" x1="0" y1="0" x2="0" y2="1">
        <stop offset="0" stop-color="#f2e8df" stop-opacity="0.55"/>
        <stop offset="0.3" stop-color="#ffffff" stop-opacity="0"/>
        <stop offset="0.85" stop-color="#c98a7a" stop-opacity="0.35"/>
      </linearGradient>
    </defs>
    <rect x="0" y="0" width="946" height="500" fill="url(#skyWarm)"/>
    <rect x="0" y="0" width="946" height="500" fill="url(#skyFade)"/>
    <path d="M0 469 Q420 525 946 402 L946 500 L0 500 Z" fill="#ffffff"/>
  </svg>

  <div class="brand-name">The Steady Harbor</div>

  <div class="slide-photo" role="img" aria-label="Sun setting over the ocean framed by tree branches and wooden posts">
    <div class="slide-caption">Seeking life coaching &amp; change consultation</div>
  </div>
  <div class="slider-dots"><span></span><span></span><span></span><span></span><span></span></div>

  <div class="hero-tagline">Compassion focused cognitive therapy to help you create meaningful positive change</div>
  <div class="hero-figure" role="img" aria-label="Silhouette of a person with raised arms"></div>

  <h1 class="welcome-title" style="margin:0;font-weight:400">Welcome The Steady Harbor</h1>

  <div class="welcome-photo" role="img" aria-label="Portrait of a smiling client"></div>
  <div class="welcome-copy">
    <p>Loren text usedI have discovered one lasting way to truly change yourself. When applied, it will transform you from the inside out and cause you to think and act differently and experience all that life has to offer. Coaching is not therapy, but a partnering relationship that leads to major changes in your life. You will be able to identify the reasons and characteristics that prevent you from living at your peak performance in the midst of life's challenges.</p>
    <p>Human nature cannot be trusted to always do the right thing. Without a solid anchor or foundation, we can drift off course in life and may even crash on the obstacles in our path.</p>
  </div>
  <div class="section-rule"></div>
  <a class="read-more-line" href="#">Read More...</a>

  <section class="feature feature-about">
    <h2>ABOUT US</h2>
    <div class="feature-text">
      <p>Loren text usedI have discovered one lasting way to truly change yourself.</p>
      <p>When applied, it will transform you from the inside out and cause you to think</p>
    </div>
    <a class="feature-link" href="#">Read More...</a>
  </section>
  <section class="feature feature-what">
    <h2>WHAT WE DO</h2>
    <div class="feature-text">
      <p>Loren text usedI have discovered one lasting way to truly change yourself.</p>
      <p>When applied, it will transform you from the inside out and cause you to think</p>
    </div>
    <a class="feature-link" href="#">Read More...</a>
  </section>
  <section class="feature feature-member">
    <h2>MEMBERSHIP</h2>
    <div class="feature-text">
      <p>Loren text usedI have discovered one lasting way to truly change yourself.</p>
      <p>When applied, it will transform you from the inside out and cause you to think</p>
    </div>
    <a class="feature-link" href="#">Read More...</a>
  </section>

  <footer class="site-footer">
    <svg class="abs" style="left:113px;top:15px" width="32" height="35" viewBox="0 0 32 35" aria-hidden="true">
      <rect x="1" y="4" width="30" height="30" rx="2" fill="#ffffff" stroke="#555555"/>
      <rect x="1" y="4" width="30" height="8" fill="#2f5fa8"/>
      <rect x="7" y="1" width="3" height="7" fill="#777777"/>
      <rect x="22" y="1" width="3" height="7" fill="#777777"/>
      <text x="16" y="29" text-anchor="middle" font-family="Open Sans, sans-serif" font-size="14" fill="#222222">14</text>
    </svg>
    <div class="footer-heading" style="left:158px;top:26px">Latest News</div>
    <div class="more-pill">more</div>

    <div class="news-item" style="top:62px">
      <div class="news-title"><span class="news-date">26/03</span> - Lorem ipsum dolor sit amet</div>
      <div class="news-by">by admin</div>
    </div>
    <div class="news-item" style="top:106px">
      <div class="news-title"><span class="news-date">26/03</span> - Lorem ipsum dolor sit amet</div>
      <div class="news-by">by admin</div>
    </div>
    <div class="news-item" style="top:151px">
      <div class="news-title"><span class="news-date">26/03</span> - Lorem ipsum dolor sit amet</div>
      <div class="news-by">by admin</div>
    </div>

    <div class="footer-divider" style="left:342px"></div>

    <svg class="abs" style="left:369px;top:17px" width="38" height="30" viewBox="0 0 38 30" aria-hidden="true">
      <rect x="2" y="5" width="32" height="22" fill="#f4f4f4" stroke="#888888"/>
      <path d="M2 5 L18 18 L34 5" fill="none" stroke="#888888"/>
    </svg>
    <div class="footer-heading" style="left:418px;top:26px">Contact Us</div>
    <div class="contact-name">Steady Harbor</div>
    <div class="contact-lines">
      Lindenlaan 42<br>
      1234 AB Veldhoven<br>
      The Netherlands<br>
      T.: 020-5550134<br>
      F.: 020-5550178<br>
      E: <a href="#">hello@steadyharbor.example</a>
    </div>
    <div class="contact-map" role="img" aria-label="Street map showing the practice location"></div>

    <div class="footer-divider" style="left:621px"></div>

    <div class="footer-brand">The Steady Harbor</div>
    <div class="copyright">Copyright © The Steady Harbor<br>All rights reserved.</div>
  </footer>

</div>
</body>
</html>
```